Animal Eye Clinic needs a Business card

We are a new veterinary ophthalmology practice (Tessaly Animal Eye Care) and we need a business card designed. We only see animal eyes - we are not a regular veterinary clinic. We already have a logo. We are looking for a professional, good looking business card to hand out to our clients. We are looking for something simple but professional and contemporary. Our logo is likely the only picture/graphic that needs to be on the card.
Updates

Contact Information for Business Card

Marisol Dunkley, BSc, DVM, MSc, DipACVO
Veterinary Ophthalmologist

Phone: 250.418.3097
Email: tessalyanimaleyecare@mailbrook.net
Website: tessalyanimaleyecare.net
Address: 1840 Pellworth Rd
Kelowna, BC, V4T 8M3

Colors

Designer to choose colors to be used in the design.

Requirements
Must have
• Our logo (attached)

```html
<!DOCTYPE html>
<html lang="en">
<head>
<meta charset="utf-8">
<title>Tessaly Animal Eye Care – Business Card</title>
<link rel="stylesheet" href="https://fonts.googleapis.com/css2?family=Archivo:wght@400;600&display=swap">
<style>
  :root {
    --stage: #2b2b2b;
    --card: #232222;
    --card-pattern-a: #2a2929;
    --card-pattern-b: #333232;
    --teal: #1b9aa6;
    --white: #f2f2f2;
    --grey: #bdbdbd;
  }
  * { box-sizing: border-box; margin: 0; padding: 0; }
  html, body { width: 1200px; height: 900px; overflow: hidden; }
  body {
    background: var(--stage);
    font-family: "Archivo", "Helvetica Neue", Arial, sans-serif;
    color: var(--white);
    position: relative;
  }
  .card {
    position: absolute;
    left: 285px;
    width: 630px;
    height: 360px;
    background: var(--card);
    border-radius: 4px;
    overflow: hidden;
  }
  .card--front { top: 60px; }
  .card--back { top: 480px; }

  /* Front */
  .front-pattern {
    position: absolute; inset: 0;
    background: linear-gradient(135deg, var(--card-pattern-a), var(--card-pattern-b) 50%, var(--card-pattern-a));
  }
  .brand {
    position: absolute;
    display: flex; align-items: center; gap: 12px;
    color: var(--teal);
    font-weight: 600;
    text-transform: uppercase;
    letter-spacing: 0.02em;
  }
  .brand__dot {
    width: 14px; height: 14px; border-radius: 50%;
    background: var(--teal);
  }
  .card--front .brand { top: 140px; left: 0; right: 0; justify-content: center; font-size: 27px; }
  .front-web {
    position: absolute; top: 206px; left: 0; right: 0;
    display: flex; justify-content: center; align-items: center; gap: 8px;
    font-size: 14px; color: var(--white);
  }
  .front-web__dot { width: 10px; height: 10px; border-radius: 50%; background: var(--teal); }

  /* Back */
  .card--back .brand { top: 86px; left: 40px; font-size: 22px; }
  .holder {
    position: absolute; top: 150px; right: 40px;
    text-align: right;
  }
  .holder__name {
    color: var(--teal);
    font-size: 23px;
    font-variant: small-caps;
    letter-spacing: 0.06em;
    font-weight: 400;
    margin-bottom: 4px;
  }
  .holder__meta { font-size: 12px; line-height: 1.45; color: var(--white); }
  .rule { position: absolute; height: 2px; background: var(--teal); }
  .rule--top { top: 232px; left: 300px; right: 40px; }
  .rule--bottom { top: 322px; left: 150px; right: 40px; }
  .contacts {
    position: absolute; top: 256px; right: 40px;
    display: flex; flex-direction: column; align-items: flex-end; gap: 8px;
    font-size: 14px;
  }
  .contacts__row { display: flex; align-items: center; gap: 16px; }
  .contact { display: flex; align-items: center; gap: 6px; }
  .contact__icon { width: 14px; height: 14px; flex: none; }
</style>
</head>
<body>

<section class="card card--front" aria-label="Business card front">
  <div class="front-pattern" role="img" aria-label="Subtle repeating tone-on-tone pattern of the clinic's mark across the card"></div>
  <div class="brand"><span class="brand__dot"></span>Tessaly Animal Eye Care</div>
  <div class="front-web"><span class="front-web__dot"></span>tessalyanimaleyecare.net</div>
</section>

<section class="card card--back" aria-label="Business card back">
  <div class="brand"><span class="brand__dot"></span>Tessaly Animal Eye Care</div>

  <div class="holder">
    <h1 class="holder__name">Marisol Dunkley</h1>
    <p class="holder__meta">BSc, DVM, MSc, DipACVO</p>
    <p class="holder__meta">Veterinary Ophthalmologist</p>
  </div>
  <div class="rule rule--top"></div>

  <div class="contacts">
    <div class="contacts__row">
      <span class="contact">
        <svg class="contact__icon" viewBox="0 0 14 14" aria-hidden="true"><circle cx="7" cy="7" r="7" fill="#1b9aa6"/><path d="M4.5 3.8c.4-.3.9-.2 1.1.2l.5 1c.1.3 0 .6-.2.8l-.4.3c.4.9 1.1 1.6 2 2l.3-.4c.2-.2.5-.3.8-.2l1 .5c.4.2.5.7.2 1.1-.5.6-1.2.8-1.9.5C6 8.9 5.1 8 4.4 6.1c-.3-.7-.1-1.5.1-2.3z" fill="#232222"/></svg>
        250.418.3097
      </span>
      <span class="contact">
        <svg class="contact__icon" viewBox="0 0 14 14" aria-hidden="true"><circle cx="7" cy="7" r="7" fill="#1b9aa6"/><path d="M7 3a2.4 2.4 0 0 0-2.4 2.4C4.6 7.2 7 10.5 7 10.5s2.4-3.3 2.4-5.1A2.4 2.4 0 0 0 7 3zm0 3.3a.9.9 0 1 1 0-1.8.9.9 0 0 1 0 1.8z" fill="#232222"/></svg>
        1840 Pellworth Rd, Kelowna, BC, V4T 8M3
      </span>
    </div>
    <span class="contact">
      <svg class="contact__icon" viewBox="0 0 14 14" aria-hidden="true"><circle cx="7" cy="7" r="7" fill="#1b9aa6"/><rect x="3.6" y="4.6" width="6.8" height="4.8" rx=".5" fill="#232222"/><path d="M3.8 5l3.2 2.3L10.2 5" stroke="#1b9aa6" stroke-width=".8" fill="none"/></svg>
      tessalyanimaleyecare@mailbrook.net
    </span>
  </div>
  <div class="rule rule--bottom"></div>
</section>

</body>
</html>
```